Entertainment Sound and Lighting company Business card

We need a professional looking business card designed for my growing entertainment sound and lighting company based in Sydney, Australia called "Kestrel Sound"

We provide technical production services (sound systems/lighting/vision) for events ranging from band gigs, weddings, corporate functions etc.

The business card needs to contain the following information:

Bartholomew Quenneville
Audio Engineer
Phone: 0478 615 702
Email: bartholomew@kestrelsound.com.au
Website: www.kestrelsound.com.au

Business logo has been attached in .ai format, please contact me if you need me to provide other files.

Target Market(s)

We need a business card that reflects our modern and professional company but still looks professional to appeal to our corporate clients.
We have a very broad target market spanning from bands needing PA systems for their gigs (18-30yrs) to event companies needing sound and lighting for weddings and other functions.

Industry/Entity Type

Business

Requirements
Must have
• Needs to include the logo that is attached of course, and the colour scheme.
Nice to have
• - Double sided

```html
<!DOCTYPE html>
<html lang="en">
<head>
<meta charset="utf-8">
<title>Kestrel Sound — Business Card</title>
<link rel="stylesheet" href="https://fonts.googleapis.com/css2?family=Arimo:wght@400;700&display=swap">
<style>
  :root {
    --page-bg: #ffffff;
    --board-top: #f4f4f4;
    --board-bottom: #e4e4e4;
    --board-edge: #a8a8a8;
    --card-bg: #ffffff;
    --ink: #111111;
    --brand-blue: #1a9ad6;
    --card-shadow: rgba(0, 0, 0, 0.28);
  }
  * { box-sizing: border-box; margin: 0; padding: 0; }
  html, body {
    width: 1050px;
    height: 1200px;
    overflow: hidden;
    background: var(--page-bg);
    font-family: "Arimo", Arial, sans-serif;
    color: var(--ink);
  }
  .board {
    position: absolute;
    left: 152px;
    top: 66px;
    width: 736px;
    height: 1060px;
    border: 1.5px solid var(--board-edge);
    border-radius: 40px;
    background: linear-gradient(180deg, var(--board-top) 0%, var(--board-bottom) 100%);
  }
  .side-label {
    position: absolute;
    left: 62px;
    font-size: 24px;
    font-weight: 400;
    color: var(--ink);
  }
  .side-label--front { top: 58px; }
  .side-label--back { top: 455px; }
  .card {
    position: absolute;
    left: 66px;
    width: 598px;
    height: 298px;
    background: var(--card-bg);
    border-radius: 28px;
    box-shadow: 6px 10px 14px var(--card-shadow);
  }
  .card--front { top: 106px; }
  .card--back { top: 498px; }
  .brand {
    position: absolute;
    right: 46px;
    top: 168px;
    display: flex;
    align-items: center;
    gap: 12px;
  }
  .brand__dot {
    width: 20px;
    height: 20px;
    border-radius: 50%;
    background: var(--brand-blue);
  }
  .brand__name {
    font-size: 30px;
    font-weight: 700;
    color: var(--brand-blue);
    letter-spacing: -0.5px;
  }
  .holder {
    position: absolute;
    left: 34px;
    top: 36px;
    font-size: 21px;
    line-height: 28px;
  }
  .holder__name { font-weight: 700; }
  .holder__role { font-weight: 400; }
  .contact {
    position: absolute;
    right: 40px;
    top: 194px;
    font-size: 20px;
    line-height: 27px;
    font-weight: 400;
  }
</style>
</head>
<body>
  <main class="board">
    <p class="side-label side-label--front">Front</p>
    <section class="card card--front" aria-label="Card front">
      <div class="brand">
        <span class="brand__dot" aria-hidden="true"></span>
        <span class="brand__name">Kestrel Sound</span>
      </div>
    </section>

    <p class="side-label side-label--back">Back</p>
    <section class="card card--back" aria-label="Card back">
      <div class="holder">
        <p class="holder__name">Bartholomew Quenneville</p>
        <p class="holder__role">Audio Engineer</p>
      </div>
      <div class="contact">
        <p>Phone: 0478 615 702</p>
        <p>bartholomew@kestrelsound.com.au</p>
        <p>www.kestrelsound.com.au</p>
      </div>
    </section>
  </main>
</body>
</html>
```